Website Design for a holiday home letting busines

We require a redesign of our present website www.birchwoodstays.com. We want the website to stand out and look professional and clean to make holiday hunters want to book a caravan or lodge holiday with us. Our logo is red however we DO NOT want the website to be red. We want a natural colour scheme.

The final design should communicate that we are a professional company to book with.

On the home page we require;
Overview of company
Photo
Search box for holiday (check in)
Late Deals
Reviews
News

We would like the following pages designed; home page, available dates page, caravans page, content page.

The website should be responsive for smart phones. One website I do like is http://www.verdamoro.be/nl/

Target Market(s)

Families

Industry/Entity Type

Travel

Number of Pages Required

5+ page

Font styles to use
Serif

Requirements
Must have
• The project must be responsive for mobile phones and tablets.
• Ability to search for holiday home holidays
• We want a natural colour scheme.
Nice to have
• A style we like is http://www.verdamoro.be/nl/
Should not have
• Do not use red as a colour for the website. Our logo is red so this is the only time we want this used.

```html
<!DOCTYPE html>
<html lang="en">
<head>
<meta charset="utf-8">
<title>Birchwood Stays – Caravan &amp; Lodge Holidays</title>
<link href="https://fonts.googleapis.com/css2?family=Montserrat:wght@400;600;700&family=Open+Sans:wght@400;600;700&family=Kaushan+Script&display=swap" rel="stylesheet">
<style>
:root{
  --blue:#3b8fd9;
  --blue-dark:#2a6fb5;
  --green:#3eaa3a;
  --green-dark:#2f8f2c;
  --ink:#333;
  --muted:#7a7a7a;
  --line:#e3e3e3;
  --footer:#2c2c2c;
  --footer-2:#232323;
  --white:#fff;
  --brand-red:#d7282f;
  --sand:#f1dfb8;
  --sky:#8fd0f2;
  --sea:#2fa6cf;
}
*{box-sizing:border-box;margin:0;padding:0}
html,body{width:1200px;height:3252px;overflow:hidden}
body{font-family:"Open Sans",Arial,sans-serif;color:var(--ink);font-size:13px;background:#fff}
h2.section-title{font-family:"Montserrat",Arial,sans-serif;font-weight:700;font-size:30px;text-align:center;text-transform:uppercase;letter-spacing:.5px}
.btn{display:inline-block;background:var(--blue);color:#fff;font-family:"Montserrat",sans-serif;font-weight:600;font-size:11px;text-transform:uppercase;padding:9px 16px;border-radius:2px}
.dots{display:flex;justify-content:center;gap:7px}
.dots span{width:8px;height:8px;border-radius:50%;background:#c9c9c9}
.dots span.on{background:var(--blue)}

/* hero */
.hero{position:relative;height:450px;overflow:hidden}
.hero-bg{position:absolute;inset:0;background:linear-gradient(180deg,var(--sky) 0%,#bfe6f8 38%,var(--sea) 40%,#5fc2dd 55%,#e8d8b0 62%,var(--sand) 100%)}
.site-header{position:absolute;top:0;left:0;right:0;height:80px;display:flex;align-items:center;padding:0 40px}
.logo{background:#fff;padding:10px 16px;display:flex;align-items:center;gap:10px;border-radius:3px;box-shadow:0 2px 6px rgba(0,0,0,.15)}
.logo-mark{width:26px;height:26px;background:var(--brand-red);border-radius:50%}
.logo-name{font-family:"Montserrat",sans-serif;font-weight:700;font-size:20px;color:var(--brand-red)}
.call{margin-left:120px;color:#fff;font-family:"Montserrat",sans-serif}
.call small{display:block;font-size:11px;font-weight:600}
.call strong{font-size:24px;font-weight:700}
.header-search{margin-left:auto;width:200px;height:32px;background:#fff;border-radius:2px;display:flex;align-items:center;justify-content:space-between;padding:0 10px;color:var(--muted);font-size:11px}
.menu-btn{margin-left:30px;border:1px solid #fff;color:#fff;font-family:"Montserrat",sans-serif;font-size:12px;font-weight:600;padding:7px 16px;display:flex;align-items:center;gap:8px}
.side-tab{position:absolute;right:0;top:160px;width:34px;height:100px;background:var(--brand-red);color:#fff;writing-mode:vertical-rl;font-family:"Montserrat",sans-serif;font-weight:700;font-size:12px;display:flex;align-items:center;justify-content:center;text-transform:uppercase}
.holiday-search{position:absolute;left:40px;top:170px;width:262px;height:270px;background:#fff;padding:16px 18px;box-shadow:0 3px 10px rgba(0,0,0,.2)}
.holiday-search h3{font-family:"Kaushan Script",cursive;font-weight:400;font-size:20px;margin-bottom:14px}
.field{display:flex;align-items:center;margin-bottom:12px;font-size:11px;color:var(--muted)}
.field label{width:70px}
.field .input{flex:1;height:24px;border:1px solid var(--line);font-size:10px;padding:4px 6px}
.field .cal{width:22px;height:24px;background:var(--green);margin-left:4px}
.holiday-search .btn{margin-top:6px}
.hero-photo{position:absolute;left:440px;top:125px;width:470px;height:250px;background:#fff;padding:10px;transform:rotate(-1.5deg);box-shadow:0 4px 14px rgba(0,0,0,.25)}
.hero-photo .fill{width:100%;height:100%;background:linear-gradient(135deg,#7cc7ea,#f3d79b 70%,#e8b86d)}
.hero-tagline{position:absolute;left:560px;top:388px;font-family:"Kaushan Script",cursive;font-size:28px;color:var(--blue-dark)}

/* intro */
.intro{height:340px;padding-top:40px;text-align:center}
.intro p{width:760px;margin:18px auto 0;font-size:12px;line-height:20px;color:var(--muted)}
.intro .btn{margin-top:26px}

/* listings */
.listings{height:440px;position:relative;padding-top:55px}
.listings-bg{position:absolute;inset:0;background:linear-gradient(120deg,#cfe9f6 0%,#f4e2a6 35%,#e9b064 55%,#b7dced 100%);opacity:.85}
.listings>*:not(.listings-bg){position:relative}
.late-deals{height:400px;padding-top:40px}
.cards{display:flex;gap:20px;width:1060px;margin:34px auto 20px}
.card{width:250px;background:#fff;border:1px solid var(--line);box-shadow:0 2px 6px rgba(0,0,0,.12)}
.card-img{height:132px;background:linear-gradient(135deg,#b98a5a,#e8d2b0 55%,#8f6a45)}
.card-body{padding:12px 14px}
.card-body h4{font-family:"Montserrat",sans-serif;font-size:13px;font-weight:700;margin-bottom:6px}
.card-body dl{display:grid;grid-template-columns:90px 1fr;font-size:10px;color:var(--muted);row-gap:3px}
.card-foot{display:flex;align-items:center;gap:14px;padding:0 14px 12px}
.card-foot svg{width:18px;height:18px}
.card-foot .btn{margin-left:auto;padding:7px 10px;font-size:9px}

/* reviews */
.reviews{height:520px;background:var(--blue);padding-top:42px;color:#fff;position:relative}
.reviews .section-title{color:#fff}
.quote-mark{text-align:center;font-family:Georgia,serif;font-size:70px;line-height:60px;margin-top:14px}
.review-row{display:flex;gap:40px;justify-content:center;margin-top:30px}
.review{width:340px;text-align:center}
.review-box{background:#fff;color:var(--muted);display:flex;gap:14px;padding:18px;text-align:left;box-shadow:0 2px 8px rgba(0,0,0,.2)}
.avatar{width:70px;height:70px;border-radius:50%;flex:none;background:linear-gradient(135deg,#c8d3dd,#9aa9b6)}
.review-box h5{color:var(--blue);font-size:12px;margin-bottom:4px}
.review-box p{font-size:10px;line-height:15px}
.review cite{display:block;margin-top:12px;font-style:normal;font-size:11px;font-weight:600}
.reviews .dots{position:absolute;bottom:34px;left:0;right:0}
.reviews .dots span{background:rgba(255,255,255,.5)}
.reviews .dots span.on{background:#fff}

/* news */
.news{height:470px;position:relative;padding-top:42px}
.news-bg{position:absolute;inset:0;background:linear-gradient(180deg,#f3f5f7,#dfe4e8)}
.news>*:not(.news-bg){position:relative}
.news-row{display:flex;gap:24px;width:840px;margin:34px auto 24px}
.news-card{width:264px;background:#fff;box-shadow:0 2px 8px rgba(0,0,0,.12)}
.news-tag{background:var(--green);color:#fff;font-size:9px;font-weight:700;text-transform:uppercase;padding:7px 12px}
.news-card .inner{padding:14px 14px 18px}
.news-card h4{font-family:"Montserrat",sans-serif;font-size:14px;font-weight:700;text-transform:uppercase;line-height:18px;margin-bottom:8px}
.news-card p{font-size:10px;line-height:15px;color:var(--muted)}
.news-card a{display:block;margin-top:10px;font-size:10px;color:var(--blue);font-weight:700;text-decoration:none}

/* newsletter */
.newsletter{height:200px;background:var(--green);text-align:center;color:#fff;padding-top:28px}
.newsletter .icon{width:44px;height:44px;border-radius:50%;border:2px solid #fff;margin:0 auto 12px;display:flex;align-items:center;justify-content:center}
.newsletter h3{font-family:"Montserrat",sans-serif;font-size:17px;font-weight:600}
.signup{display:flex;justify-content:center;margin-top:18px}
.signup .input{width:260px;height:32px;background:#fff;color:var(--muted);font-size:10px;text-align:left;padding:10px 12px}
.signup .btn{background:var(--blue);border-radius:0;padding:10px 16px}

/* footer */
.site-footer{height:432px;background:var(--footer);color:#bbb;padding:30px 110px 0;position:relative}
.footer-cols{display:flex;gap:60px}
.site-footer h4{color:#fff;font-family:"Montserrat",sans-serif;font-size:16px;margin-bottom:12px}
.link-cols{display:flex;gap:34px;font-size:10px;line-height:18px}
.link-cols ul{list-style:none}
.social li{list-style:none;display:flex;align-items:center;gap:8px;font-size:10px;line-height:22px}
.social i{width:14px;height:14px;border-radius:50%;background:#555;display:inline-block}
.badge{width:90px;height:90px;border-radius:50%;background:#3f7f3c;border:4px solid #fff;margin-left:30px;margin-top:8px}
.footer-note{margin-top:34px;font-size:10px;line-height:16px;width:980px}
.copyright{position:absolute;left:0;right:0;bottom:0;height:40px;background:var(--footer-2);font-size:10px;text-align:center;line-height:40px}
</style>
</head>
<body>

<section class="hero">
  <div class="hero-bg" role="img" aria-label="Sunny beach with sea, sand, parasol and palm tree"></div>
  <header class="site-header">
    <div class="logo"><span class="logo-mark"></span><span class="logo-name">Birchwood Stays</span></div>
    <div class="call"><small>CALL US</small><strong>07700 900 412</strong></div>
    <div class="header-search">Search Here
      <svg width="12" height="12" viewBox="0 0 12 12"><circle cx="5" cy="5" r="3.5" fill="none" stroke="#999" stroke-width="1.5"/><line x1="7.5" y1="7.5" x2="11" y2="11" stroke="#999" stroke-width="1.5"/></svg>
    </div>
    <div class="menu-btn"><svg width="14" height="10"><rect width="14" height="2" fill="#fff"/><rect y="4" width="14" height="2" fill="#fff"/><rect y="8" width="14" height="2" fill="#fff"/></svg>MENU</div>
  </header>
  <div class="side-tab">Book Now</div>

  <form class="holiday-search">
    <h3>Holiday Search</h3>
    <div class="field"><label>Check in</label><div class="input">DD / MM / YYYY</div><span class="cal"></span></div>
    <div class="field"><label>Check out</label><div class="input">DD / MM / YYYY</div><span class="cal"></span></div>
    <div class="field"><label>Adults</label><div class="input">2</div></div>
    <div class="field"><label>Children</label><div class="input">0</div></div>
    <span class="btn">Search</span>
  </form>

  <div class="hero-photo"><div class="fill" role="img" aria-label="Happy children in sunglasses relaxing on the beach"></div></div>
  <div class="hero-tagline">Private Holiday Rentals!</div>
</section>

<section class="intro">
  <h2 class="section-title">No Deposit Holidays</h2>
  <p>Book your stay at Larchmere Bay with no deposit to pay today. Choose from our caravans and lodges, secure the dates you want and settle the balance closer to your break.</p>
  <p>We have flexible pay-as-you-go options across all our holiday homes, so you can plan ahead without a large upfront cost and enjoy the peace of mind of booking direct.</p>
  <span class="btn">Read More</span>
</section>

<section class="listings">
  <div class="listings-bg" role="img" aria-label="Soft blurred beach ball on golden sand"></div>
  <h2 class="section-title">Our Caravans and Lodges</h2>
  <div class="cards">
    <article class="card"><div class="card-img" role="img" aria-label="Caravan living room interior"></div><div class="card-body"><h4>New Hollyfield</h4><dl><dt>Caravan type</dt><dd>Deluxe</dd><dt>Sleeps</dt><dd>6 guests</dd></dl></div><div class="card-foot"><svg viewBox="0 0 18 18"><rect x="2" y="6" width="14" height="9" fill="none" stroke="#999"/></svg><svg viewBox="0 0 18 18"><circle cx="9" cy="9" r="6" fill="none" stroke="#999"/></svg><span class="btn">Book Dates</span></div></article>
    <article class="card"><div class="card-img" role="img" aria-label="Lodge lounge interior"></div><div class="card-body"><h4>New Hollyfield</h4><dl><dt>Caravan type</dt><dd>Deluxe</dd><dt>Sleeps</dt><dd>6 guests</dd></dl></div><div class="card-foot"><svg viewBox="0 0 18 18"><rect x="2" y="6" width="14" height="9" fill="none" stroke="#999"/></svg><svg viewBox="0 0 18 18"><circle cx="9" cy="9" r="6" fill="none" stroke="#999"/></svg><span class="btn">Book Dates</span></div></article>
    <article class="card"><div class="card-img" role="img" aria-label="Caravan living room interior"></div><div class="card-body"><h4>New Hollyfield</h4><dl><dt>Caravan type</dt><dd>Deluxe</dd><dt>Sleeps</dt><dd>6 guests</dd></dl></div><div class="card-foot"><svg viewBox="0 0 18 18"><rect x="2" y="6" width="14" height="9" fill="none" stroke="#999"/></svg><svg viewBox="0 0 18 18"><circle cx="9" cy="9" r="6" fill="none" stroke="#999"/></svg><span class="btn">Book Dates</span></div></article>
    <article class="card"><div class="card-img" role="img" aria-label="Lodge lounge interior"></div><div class="card-body"><h4>New Hollyfield</h4><dl><dt>Caravan type</dt><dd>Deluxe</dd><dt>Sleeps</dt><dd>6 guests</dd></dl></div><div class="card-foot"><svg viewBox="0 0 18 18"><rect x="2" y="6" width="14" height="9" fill="none" stroke="#999"/></svg><svg viewBox="0 0 18 18"><circle cx="9" cy="9" r="6" fill="none" stroke="#999"/></svg><span class="btn">Book Dates</span></div></article>
  </div>
  <div class="dots"><span class="on"></span><span></span><span></span><span></span></div>
</section>

<section class="late-deals">
  <h2 class="section-title">Late Deals</h2>
  <div class="cards">
    <article class="card"><div class="card-img" role="img" aria-label="Caravan living room interior"></div><div class="card-body"><h4>New Hollyfield</h4><dl><dt>Caravan type</dt><dd>Deluxe</dd><dt>Price</dt><dd>From £199</dd></dl></div><div class="card-foot"><svg viewBox="0 0 18 18"><rect x="2" y="6" width="14" height="9" fill="none" stroke="#999"/></svg><svg viewBox="0 0 18 18"><circle cx="9" cy="9" r="6" fill="none" stroke="#999"/></svg><span class="btn">Book Dates</span></div></article>
    <article class="card"><div class="card-img" role="img" aria-label="Lodge lounge interior"></div><div class="card-body"><h4>New Hollyfield</h4><dl><dt>Caravan type</dt><dd>Deluxe</dd><dt>Price</dt><dd>From £199</dd></dl></div><div class="card-foot"><svg viewBox="0 0 18 18"><rect x="2" y="6" width="14" height="9" fill="none" stroke="#999"/></svg><svg viewBox="0 0 18 18"><circle cx="9" cy="9" r="6" fill="none" stroke="#999"/></svg><span class="btn">Book Dates</span></div></article>
    <article class="card"><div class="card-img" role="img" aria-label="Caravan living room interior"></div><div class="card-body"><h4>New Hollyfield</h4><dl><dt>Caravan type</dt><dd>Deluxe</dd><dt>Price</dt><dd>From £199</dd></dl></div><div class="card-foot"><svg viewBox="0 0 18 18"><rect x="2" y="6" width="14" height="9" fill="none" stroke="#999"/></svg><svg viewBox="0 0 18 18"><circle cx="9" cy="9" r="6" fill="none" stroke="#999"/></svg><span class="btn">Book Dates</span></div></article>
    <article class="card"><div class="card-img" role="img" aria-label="Lodge lounge interior"></div><div class="card-body"><h4>New Hollyfield</h4><dl><dt>Caravan type</dt><dd>Deluxe</dd><dt>Price</dt><dd>From £199</dd></dl></div><div class="card-foot"><svg viewBox="0 0 18 18"><rect x="2" y="6" width="14" height="9" fill="none" stroke="#999"/></svg><svg viewBox="0 0 18 18"><circle cx="9" cy="9" r="6" fill="none" stroke="#999"/></svg><span class="btn">Book Dates</span></div></article>
  </div>
  <div class="dots"><span class="on"></span><span></span></div>
</section>

<section class="reviews">
  <h2 class="section-title">Latest Reviews</h2>
  <div class="quote-mark">&ldquo;</div>
  <div class="review-row">
    <div class="review"><div class="review-box"><div class="avatar" role="img" aria-label="Guest portrait"></div><div><h5>Stayed in New Hollyfield</h5><p>Lovely clean caravan with everything we needed. The kids loved the park and we will be booking again next summer without a doubt.</p></div></div><cite>&mdash; Customer Review</cite></div>
    <div class="review"><div class="review-box"><div class="avatar" role="img" aria-label="Guest portrait"></div><div><h5>Stayed in New Hollyfield</h5><p>Friendly owners, easy booking and a spotless lodge. A relaxing week by the sea that the whole family enjoyed from start to finish.</p></div></div><cite>&mdash; Customer Review</cite></div>
  </div>
  <div class="dots"><span class="on"></span><span></span><span></span></div>
</section>

<section class="news">
  <div class="news-bg" role="img" aria-label="Faded laptop on a desk"></div>
  <h2 class="section-title">Latest News</h2>
  <div class="news-row">
    <article class="news-card"><div class="news-tag">Posted on 14 August in Events</div><div class="inner"><h4>Sunny Days Show Live at Larchmere Bay</h4><p>A family stage show comes to the park this summer with songs, dancing and fun for children of all ages.</p><a>Read More...</a></div></article>
    <article class="news-card"><div class="news-tag">Posted on 14 August in Events</div><div class="inner"><h4>Sunny Days Show Live at Larchmere Bay</h4><p>A family stage show comes to the park this summer with songs, dancing and fun for children of all ages.</p><a>Read More...</a></div></article>
    <article class="news-card"><div class="news-tag">Posted on 14 August in Events</div><div class="inner"><h4>Sunny Days Show Live at Larchmere Bay</h4><p>A family stage show comes to the park this summer with songs, dancing and fun for children of all ages.</p><a>Read More...</a></div></article>
  </div>
  <div class="dots"><span class="on"></span><span></span><span></span></div>
</section>

<section class="newsletter">
  <div class="icon"><svg width="20" height="14" viewBox="0 0 20 14"><rect x="1" y="1" width="18" height="12" fill="none" stroke="#fff" stroke-width="1.5"/><polyline points="1,1 10,8 19,1" fill="none" stroke="#fff" stroke-width="1.5"/></svg></div>
  <h3>Subscribe our newsletter to get the best deals and offers!</h3>
  <div class="signup"><div class="input">ENTER YOUR EMAIL ID</div><span class="btn">Subscribe</span></div>
</section>

<footer class="site-footer">
  <div class="footer-cols">
    <div>
      <h4>Quick Links</h4>
      <div class="link-cols">
        <ul><li>About us</li><li>News</li><li>Caravans &amp; Lodges</li><li>Late Deals</li><li>Available Dates</li><li>Contact Us</li></ul>
        <ul><li>Larchmere Bay</li><li>Local Attractions</li><li>Terms of Use</li><li>Privacy Policy</li><li>Reviews</li><li>Park Facilities</li></ul>
        <ul><li>Booking Guide</li><li>Owner Information</li><li>Guest Handbook</li><li>Holiday Offers</li><li>Site Map</li></ul>
      </div>
    </div>
    <div style="margin-left:auto;display:flex">
      <div>
        <h4>Stay Connected</h4>
        <ul class="social"><li><i></i>Our Page</li><li><i></i>Updates</li><li><i></i>Photos</li><li><i></i>Videos</li></ul>
      </div>
      <div class="badge" role="img" aria-label="Guest rating award badge"></div>
    </div>
  </div>
  <p class="footer-note">Birchwood Stays is an independent holiday home letting business offering privately owned caravans and lodges at Larchmere Bay. All bookings are made directly with us and are not connected with the park operator. Prices and availability may change without notice.</p>
  <div class="copyright">Copyright &copy; 2015 www.birchwoodstays.com. All Rights Reserved. Privacy Policy | Terms &amp; Conditions</div>
</footer>

</body>
</html>
```